Zielgruppe
Ich biete Employer-Branding-Beratung für mittelständische Unternehmen, d.h. ich entwickle für und mit meinen Kunden ihre Arbeitgebermarke und Arbeitgeberkommunikation, um leichter neue Mitarbeitende zu finden.
Meine Zielgruppe: mittelständische Unternehmen (1.000-4.000 Mitarbeitende), dort v.a. die Personalabteilung, meist Frauen
Aufgabenstellung
- Klappkarte im Format DIN lang. Die Karte soll sich dafür eignen, sie auf den Schreibtisch zu stellen.
- Corporate Design siehe Anhang. Darin ist bereits ein Entwurf für eine Karte enthalten. Der darf gern genau so übernommen werden. Ich freue mich aber auch über gute neue Entwürfe, die das CD aufgreifen.
- Seite 1: Logo & Zitat & Autor: 'Wege entstehen dadurch, dass man sie geht.' // Gottlieb Marwen
- Seite 2: Text: Auf ein Jahr 2024 mit neuen Wegen!
- Seite 3: leer
- Seite 4: Adresse/Kontaktdaten:
Roswitha Klemm
Die Fachkräfte-Lotsin
Lindhorster Weg 23
10115 Berlin
T +49 (17 23) 592 40 17
E rk@die-fachkraefte-lotsin.de
Hinweis: Die Karte wird in durchsichtigen Umschlägen verschickt, die Adresse sollte so kontrastreich sein, dass man sie auch durch den Umschläge sehen kann, falls Briefe zurück kommen.

```html
<!DOCTYPE html>
<html lang="de">
<head>
<meta charset="utf-8">
<title>Klappkarte DIN lang – Neujahr 2024</title>
<link rel="stylesheet" href="https://fonts.googleapis.com/css2?family=Lato:ital,wght@0,300;0,400;0,700;1,400&display=swap">
<style>
  :root {
    --backdrop: #e2e2e1;
    --plum-deep: #44102b;
    --plum: #561638;
    --plum-light: #6f2b53;
    --ring: rgba(140, 60, 105, 0.28);
    --gold: #9a7328;
    --white: #ffffff;
    --panel-w: 250px;
    --panel-h: 530px;
  }
  * { box-sizing: border-box; margin: 0; padding: 0; }
  html, body {
    width: 857px;
    height: 1200px;
    overflow: hidden;
    background: var(--backdrop);
    font-family: "Lato", sans-serif;
    color: var(--white);
  }
  .spread {
    position: absolute;
    left: 178px;
    width: calc(var(--panel-w) * 2);
    height: var(--panel-h);
    display: flex;
    box-shadow: 0 6px 18px rgba(0, 0, 0, 0.18);
  }
  .spread--outside { top: 45px; }
  .spread--inside { top: 625px; }
  .panel {
    position: relative;
    width: var(--panel-w);
    height: var(--panel-h);
    overflow: hidden;
    background: linear-gradient(160deg, var(--plum-deep) 0%, var(--plum) 55%, var(--plum-light) 100%);
  }
  .panel + .panel { border-left: 1px solid rgba(0, 0, 0, 0.15); }
  .panel__rings {
    position: absolute;
    inset: 0;
    width: 100%;
    height: 100%;
  }

  /* Back page: contact block */
  .contact {
    position: absolute;
    left: 26px;
    bottom: 42px;
    font-size: 9.5px;
    line-height: 1.4;
    font-weight: 400;
  }
  .contact__address { margin-bottom: 9px; }
  .contact__row { display: flex; gap: 8px; }
  .contact__label { width: 20px; }

  /* Front page: brand + quote */
  .brand {
    position: absolute;
    top: 44px;
    right: 24px;
    display: flex;
    align-items: center;
    gap: 8px;
    font-size: 11px;
    font-weight: 400;
    letter-spacing: 0.14em;
    text-transform: uppercase;
  }
  .brand__dot {
    width: 18px;
    height: 18px;
    border: 1.5px solid var(--white);
    border-radius: 50%;
  }
  .quote {
    position: absolute;
    left: 30px;
    top: 130px;
    right: 16px;
  }
  .quote__mark {
    font-weight: 700;
    font-size: 64px;
    line-height: 0.6;
    height: 34px;
    color: var(--gold);
  }
  .quote__text {
    margin-top: 10px;
    font-weight: 300;
    font-size: 29px;
    line-height: 1.08;
    text-transform: uppercase;
  }
  .quote__author {
    margin-top: 22px;
    font-weight: 400;
    font-size: 14px;
    letter-spacing: 0.02em;
    text-transform: uppercase;
  }

  /* Inside left page: greeting */
  .greeting {
    position: absolute;
    left: 0;
    right: 0;
    top: 190px;
    text-align: center;
    text-transform: uppercase;
  }
  .greeting__line {
    font-weight: 400;
    font-size: 19px;
    letter-spacing: 0.05em;
    line-height: 1.2;
  }
  .greeting__year {
    font-weight: 300;
    font-size: 62px;
    line-height: 1.05;
    color: var(--gold);
    letter-spacing: 0.02em;
  }
</style>
</head>
<body>

<section class="spread spread--outside" aria-label="Außenseite">
  <article class="panel panel--back">
    <svg class="panel__rings" viewBox="0 0 250 530" aria-hidden="true">
      <circle cx="330" cy="300" r="200" fill="none" stroke="var(--ring)" stroke-width="34"/>
    </svg>
    <address class="contact" style="font-style: normal;">
      <p class="contact__address">Roswitha Klemm<br>Die Fachkräfte-Lotsin<br>Lindhorster Weg 23<br>10115 Berlin</p>
      <p class="contact__row"><span class="contact__label">Tel:</span><span>+49 (17 23) 592 40 17</span></p>
      <p class="contact__row"><span class="contact__label">M:</span><span>rk@die-fachkraefte-lotsin.de</span></p>
      <p class="contact__row"><span class="contact__label">W:</span><span>www.die-fachkraefte-lotsin.de</span></p>
    </address>
  </article>

  <article class="panel panel--front">
    <svg class="panel__rings" viewBox="0 0 250 530" aria-hidden="true">
      <circle cx="130" cy="290" r="170" fill="none" stroke="var(--ring)" stroke-width="30"/>
    </svg>
    <div class="brand">
      <span class="brand__dot"></span>
      <span class="brand__name">Die Fachkräfte-Lotsin</span>
    </div>
    <blockquote class="quote">
      <div class="quote__mark">“</div>
      <p class="quote__text">Wege<br>entstehen<br>dadurch,<br>dass man<br>sie geht.</p>
      <footer class="quote__author">Gottlieb Marwen</footer>
    </blockquote>
  </article>
</section>

<section class="spread spread--inside" aria-label="Innenseite">
  <article class="panel panel--greeting">
    <svg class="panel__rings" viewBox="0 0 250 530" aria-hidden="true">
      <circle cx="120" cy="260" r="175" fill="none" stroke="var(--ring)" stroke-width="30"/>
    </svg>
    <div class="greeting">
      <p class="greeting__line">Auf ein Jahr</p>
      <p class="greeting__year">2024</p>
      <p class="greeting__line">Mit neuen<br>Wegen!</p>
    </div>
  </article>
  <article class="panel panel--blank" aria-label="Leere Seite"></article>
</section>

</body>
</html>
```